Business Card for Jewelry Business

We need a new namecard design for a jewelry company based in Bangkok, Thailand. We have a new website recently and want the new namecard to reflect our new modern image. I have uploaded our old namecard to show you the information that needs to be on the namecard. Pls check our website www.qelnotrax.com for the new color scheme to help design the new namecard.

```html
<!DOCTYPE html>
<html lang="en">
<head>
<meta charset="utf-8">
<title>Qelnotrax Makers – Business Card</title>
<link rel="stylesheet" href="https://fonts.googleapis.com/css2?family=Arimo:wght@400;700&display=swap">
<style>
  :root {
    --teal: #4fc4ca;
    --ink: #2b2b2b;
    --rule: #555555;
    --paper: #ffffff;
    --backdrop: #e6e5e3;
  }
  * { margin: 0; padding: 0; box-sizing: border-box; }
  html, body { width: 1200px; height: 801px; overflow: hidden; }
  body {
    background: var(--backdrop);
    font-family: "Arimo", Arial, sans-serif;
    color: var(--ink);
    position: relative;
  }
  .card {
    position: absolute;
    top: 245px;
    width: 540px;
    height: 310px;
    box-shadow: 0 6px 18px rgba(0,0,0,0.18);
    overflow: hidden;
  }
  .card-front { left: 45px; background: var(--paper); }
  .card-back { left: 615px; background: var(--teal); }

  .brand { position: absolute; display: flex; align-items: center; gap: 12px; }
  .brand-dot { border-radius: 50%; flex: none; }
  .brand-name {
    font-weight: 400; letter-spacing: 2px;
    text-transform: uppercase; white-space: nowrap;
  }

  /* front */
  .front-brand { top: 40px; right: 36px; }
  .front-brand .brand-dot { width: 30px; height: 30px; background: var(--teal); }
  .front-brand .brand-name { font-size: 22px; color: var(--ink); }

  .person { position: absolute; left: 24px; top: 92px; }
  .person-name {
    color: var(--teal); font-weight: 700; font-size: 19px;
    text-transform: uppercase; letter-spacing: 0.5px; white-space: nowrap;
  }
  .person-title { font-size: 11.5px; margin-top: 4px; white-space: nowrap; }

  .front-rule {
    position: absolute; left: 24px; right: 24px; top: 146px;
    border-top: 1px solid var(--rule);
  }
  .front-columns {
    position: absolute; left: 24px; right: 24px; top: 158px;
    display: flex;
  }
  .col { padding: 0 12px; min-height: 84px; white-space: nowrap; }
  .col + .col { border-left: 1px solid var(--rule); }
  .col-person { padding-left: 0; width: 155px; }
  .col-company { width: 190px; }
  .col-web { flex: 1; }
  .company-name { color: var(--teal); font-size: 12px; margin-bottom: 4px; }
  .address { font-size: 11.5px; line-height: 1.45; }
  .contact-list { list-style: none; font-size: 11.5px; line-height: 1.6; }
  .contact-list li { display: flex; align-items: center; gap: 6px; }
  .contact-list svg { width: 11px; height: 11px; flex: none; }
  .social-mark {
    width: 10px; height: 10px; border-radius: 50%;
    background: var(--teal); flex: none;
  }
  .front-band {
    position: absolute; left: 0; right: 0; bottom: 0; height: 10px;
    background: var(--teal);
  }

  /* back */
  .back-brand { top: 52px; right: 40px; gap: 14px; }
  .back-brand .brand-dot { background: var(--paper); width: 28px; height: 28px; }
  .back-brand .brand-name { color: var(--paper); font-size: 30px; }
</style>
</head>
<body>

<section class="card card-front" aria-label="Card front">
  <div class="brand front-brand">
    <span class="brand-dot"></span>
    <span class="brand-name">Qelnotrax Makers</span>
  </div>

  <div class="person">
    <p class="person-name">Nira Pantawong</p>
    <p class="person-title">Sales &amp; Product Development Manager</p>
  </div>

  <div class="front-rule"></div>

  <div class="front-columns">
    <div class="col col-person">
      <ul class="contact-list">
        <li>
          <svg viewBox="0 0 12 12"><path d="M3 1 L5 3.5 L4 5 Q5.5 7.5 7 8 L8.5 7 L11 9 L9.5 11 Q4 10 1 3 Z" fill="var(--teal)"/></svg>
          +662-418-2057
        </li>
        <li>
          <svg viewBox="0 0 12 12"><rect x="1" y="4" width="10" height="7" rx="1" fill="var(--teal)"/><rect x="3" y="1" width="6" height="3" fill="var(--teal)"/></svg>
          662-5170394
        </li>
        <li>
          <svg viewBox="0 0 12 12"><rect x="1" y="2.5" width="10" height="7" fill="none" stroke="var(--teal)" stroke-width="1.2"/><path d="M1 2.5 L6 7 L11 2.5" fill="none" stroke="var(--teal)" stroke-width="1.2"/></svg>
          nira@qelnotrax.com
        </li>
        <li>
          <svg viewBox="0 0 12 12"><rect x="1" y="2.5" width="10" height="7" fill="none" stroke="var(--teal)" stroke-width="1.2"/><path d="M1 2.5 L6 7 L11 2.5" fill="none" stroke="var(--teal)" stroke-width="1.2"/></svg>
          hello@qelnotrax.com
        </li>
      </ul>
    </div>

    <div class="col col-company">
      <p class="company-name">Qelnotrax Makers Co., Ltd</p>
      <p class="address">128 Moo 7 Sukprasert Road,<br>Nong Phrai Business Park,<br>Bangkok, 10730 Thailand</p>
    </div>

    <div class="col col-web">
      <ul class="contact-list">
        <li>
          <svg viewBox="0 0 12 12"><circle cx="6" cy="6" r="5" fill="none" stroke="var(--teal)" stroke-width="1.2"/><ellipse cx="6" cy="6" rx="2.2" ry="5" fill="none" stroke="var(--teal)"/><path d="M1 6 H11" stroke="var(--teal)"/></svg>
          www.qelnotrax.com
        </li>
        <li><span class="social-mark"></span>Qelnotrax Makers</li>
        <li><span class="social-mark"></span>@qelnotraxMk</li>
      </ul>
    </div>
  </div>

  <div class="front-band"></div>
</section>

<section class="card card-back" aria-label="Card back">
  <div class="brand back-brand">
    <span class="brand-dot"></span>
    <span class="brand-name">Qelnotrax Makers</span>
  </div>
</section>

</body>
</html>
```